StartFirmo.eu - need to polish our homepage (layout only)

We run a website project (http://cz.StartFirmo.eu) enabling free company formations via the Internet.

We now do complete redesign of the website which is almost ready but we still cannot get to proper shape of the homepage and we kindly ask you to participate on finalisation of this.

What we have now:
- design of sub-pages (see attached as NewSubPage design)

What must be preserved on homepage:
- upper horizontal menu and everything above it (logo, sign in button etc.)
- bottom quick navigation menu

What we would like to have (see attached HPSketch):
- unlike current homepage (http://cz.StartFirmo.eu) some introductory section just below the upper horizontal menu which will contain catching words/references

- more detailed website description and left navigation below this introductory section

- right banners stating amount of statutory fees and costs for registered office (if one chooses so)

- section for news

Thank you in advance for your proposals. In case of any queries please let us know.
Updates

Hello designers,

Many thanks for your first proposals, just.two general comments before I comment on particular designs:

1) We will probably want that the website does NOT include images of people but rather keep it as purely informative. The reason is that as we provide free service users often take us as sort of governmental agency and for such it is not very common here to have such type of public images on the website.

2) We will have 2 banners positions for our partners, one 970x200 leaderboard on the top of webpage and one left square below left navigation. You do not need to include them in your proposals, I am just mentioning this that this space must be left free for this purpose.

Many thanks for your effort so far, I will also comment separately on your particular designs.

Lukas

Requirements
Nice to have
• - you may consider substituting bullets in short catching sentences in introductory section by some icons expressing nature of the sentence

```html
<!DOCTYPE html>
<html lang="en">
<head>
<meta charset="utf-8">
<title>StartFirmo.eu – Free Company Formation Online</title>
<link href="https://fonts.googleapis.com/css2?family=Open+Sans:wght@400;600;700&family=Roboto+Condensed:wght@300;400;700&family=Oswald:wght@300;400&display=swap" rel="stylesheet">
<style>
:root{
  --page-bg:#eceef1;
  --white:#ffffff;
  --blue:#1f5fae;
  --blue-dark:#184c8f;
  --blue-deep:#0f3f7a;
  --navy:#13306a;
  --link:#1a62b8;
  --text:#555a61;
  --muted:#8c9198;
  --line:#dfe2e6;
  --teal:#2aa99a;
  --teal-dark:#1f8f82;
  --orange:#f2901f;
  --orange-dark:#e27c10;
  --yellow:#f7b51d;
  --green-tick:#6aa83a;
  --hero-a:#e9f0f7;
  --hero-b:#f7f9fc;
}
*{box-sizing:border-box;margin:0;padding:0}
html,body{width:737px;height:1200px;overflow:hidden}
body{background:var(--page-bg);font-family:"Open Sans",Arial,sans-serif;color:var(--text);position:relative}
.top-strip{position:absolute;left:0;top:0;width:737px;height:5px;background:var(--blue)}
.sheet{position:absolute;left:83px;top:15px;width:571px;height:1030px;background:var(--white);border:1px solid #e2e4e8}
.abs{position:absolute}
.banner-slot{left:89px;top:22px;width:559px;height:116px;border:1px solid var(--line);display:flex;align-items:center;justify-content:center;font-size:9px;color:#b4b8bd;background:#fff}

/* header */
.brand{left:89px;top:164px;display:flex;align-items:center;gap:6px}
.brand-mark{width:26px;height:20px;background:var(--blue)}
.brand-name{font-family:"Roboto Condensed",Arial,sans-serif;font-weight:700;font-size:21px;color:var(--blue);letter-spacing:.2px}
.contact{left:381px;top:161px;font-size:9.5px;color:var(--link);font-weight:600;line-height:16px}
.contact div{display:flex;align-items:center;gap:9px}
.contact svg{width:11px;height:11px}
.btn{font-family:"Roboto Condensed",Arial,sans-serif;font-size:11px;border-radius:3px;display:flex;align-items:center;justify-content:center;white-space:nowrap}
.btn-signin{left:539px;top:167px;width:51px;height:18px;background:linear-gradient(var(--teal),var(--teal-dark));color:#fff}
.btn-new{left:595px;top:167px;width:53px;height:18px;background:linear-gradient(#ffd04a,var(--yellow));color:#5a3b00}

.mainnav{left:89px;top:209px;width:559px;height:28px;background:linear-gradient(#2b6cbd,var(--blue-dark));border-radius:2px;display:flex;align-items:center}
.mainnav a{font-family:"Roboto Condensed",Arial,sans-serif;font-size:9.5px;color:#fff;text-decoration:none;padding:0 17px;height:28px;line-height:28px;border-right:1px solid rgba(255,255,255,.18);letter-spacing:.3px}
.nav-tools{position:absolute;right:18px;top:6px;display:flex;gap:8px;align-items:center}
.lang{width:26px;height:14px;border:1px solid rgba(255,255,255,.6);border-radius:2px;display:flex;align-items:center;justify-content:center;gap:3px}

/* hero */
.hero{left:89px;top:247px;width:559px;height:222px;border:1px solid var(--line);background:linear-gradient(90deg,var(--hero-b) 0%,var(--hero-a) 100%);overflow:hidden}
.hero-photo{position:absolute;left:230px;top:0;width:240px;height:222px;background:radial-gradient(ellipse at 50% 45%,rgba(185,200,218,.55),rgba(233,240,247,0) 70%)}
.hero-title{position:absolute;left:15px;top:20px;font-family:"Roboto Condensed",Arial,sans-serif;font-size:22px;color:var(--navy);font-weight:700}
.hero-title span{font-weight:300}
.perks{position:absolute;left:17px;top:59px;list-style:none;font-family:"Roboto Condensed",Arial,sans-serif;font-size:11.5px;color:#2e3a4c}
.perks li{display:flex;align-items:center;gap:10px;height:22px}
.perks svg{width:12px;height:10px}
.cta{position:absolute;top:170px;height:28px;border-radius:3px;display:flex;align-items:center;justify-content:space-between;padding:0 9px 0 11px;font-family:"Roboto Condensed",Arial,sans-serif;font-weight:700;font-size:11.5px;white-space:nowrap;letter-spacing:-.1px}
.cta i{flex:none;width:13px;height:13px;border-radius:50%;background:rgba(255,255,255,.75);display:block}
.cta-try{left:17px;width:169px;background:linear-gradient(var(--teal),var(--teal-dark));color:#fff}
.cta-how{left:196px;width:98px;background:linear-gradient(#ffc93a,var(--orange));color:#3d2500}
.stats{position:absolute;left:400px;top:30px;width:130px;text-align:center;font-family:"Roboto Condensed",Arial,sans-serif;color:var(--navy)}
.stats .lbl{font-size:14px;font-weight:300}
.stats .num{font-size:14px;font-weight:700}
.stats .testi{font-size:13px;font-weight:300;margin-top:13px}
.seal{position:absolute;border-radius:50%}

/* body columns */
.sidenav{left:89px;top:489px;width:128px;height:286px;background:#f4f5f6;border:1px solid #e6e8ea}
.sidenav ul{list-style:none;margin:6px 5px 0;background:#fff;border:1px solid #e4e6e9}
.sidenav li{height:22.4px;border-bottom:1px solid #ebedef;font-size:8.5px;color:var(--muted);display:flex;align-items:center;gap:8px;padding-left:10px}
.sidenav li:last-child{border-bottom:0}
.sidenav li::before{content:"";border-left:3px solid #b8bcc1;border-top:2.5px solid transparent;border-bottom:2.5px solid transparent}
.sidenav li.active{color:var(--orange)}
.sidenav li.active::before{border-left-color:var(--orange)}
.square-slot{position:absolute;left:5px;top:157px;width:116px;height:116px;background:#fff;border:1px solid #e4e6e9;display:flex;align-items:center;justify-content:center;font-size:8px;color:#b4b8bd}

.why{left:229px;top:487px;width:251px}
.why h2{font-family:"Roboto Condensed",Arial,sans-serif;font-size:12px;color:var(--navy);font-weight:700;padding-bottom:5px;border-bottom:1px solid var(--line);position:relative;margin-bottom:4px}
.why h2::after{content:"";position:absolute;left:0;bottom:-2px;width:46px;height:3px;background:var(--navy)}
.why-item{display:flex;gap:9px;font-size:7.6px;line-height:12px;color:var(--text);margin-top:11px}
.why-item svg{flex:none;width:9px;height:7px;margin-top:3px}

.promo{left:498px;width:150px;height:127px;border-radius:2px;color:#fff;text-align:center;font-family:"Roboto Condensed",Arial,sans-serif}
.promo-statutory{top:506px;background:var(--teal)}
.promo-office{top:644px;background:var(--orange)}
.promo h3{font-family:"Oswald",Arial,sans-serif;font-weight:300;font-size:28px;line-height:30px;margin-top:10px}
.promo p.sub{font-size:10.5px;margin-top:1px}
.promo .rows{margin-top:22px;text-align:left;font-size:9px;white-space:nowrap}
.promo .row{display:flex;align-items:center;height:20px;padding-left:9px}
.promo .row b{font-weight:400;width:39px;display:flex;align-items:center;gap:5px}
.promo .row b::before{content:"";border-left:5px solid rgba(255,255,255,.8);border-top:3px solid transparent;border-bottom:3px solid transparent}

.divider-shadow{left:120px;top:805px;width:500px;height:10px;background:radial-gradient(ellipse at 50% 0%,rgba(0,0,0,.08),rgba(0,0,0,0) 70%)}

.news{left:96px;top:829px;width:544px}
.news h2{font-family:"Roboto Condensed",Arial,sans-serif;font-size:12.5px;color:var(--navy);font-weight:700;padding-bottom:5px;border-bottom:1px solid var(--line)}
.news-item{padding:0 0 12px;border-bottom:1px dotted #d5d8dc;margin-top:14px}
.news-item:last-of-type{border-bottom:0}
.news-date{font-size:7px;color:var(--muted)}
.news-title{font-size:8.5px;color:var(--link);font-weight:600;margin:8px 0 3px 1px}
.news-text{font-size:7.8px;line-height:12.5px;color:var(--text)}
.btn-more{left:96px;top:1012px;width:61px;height:19px;background:linear-gradient(#ffd04a,var(--yellow));border-radius:2px;color:#4a3000;font-family:"Roboto Condensed",Arial,sans-serif;font-size:9.5px}

/* footer */
.footer{left:0;top:1057px;width:737px;height:143px;background:linear-gradient(var(--blue),var(--blue-dark))}
.footer-bottom{position:absolute;left:0;bottom:0;width:737px;height:28px;background:var(--blue-deep);font-size:7.5px;color:#c9d8ee;padding:11px 0 0 89px}
.fcol{position:absolute;top:17px;height:97px;padding-right:10px}
.fcol + .fcol{border-left:1px solid rgba(255,255,255,.1)}
.fcol h4{font-family:"Roboto Condensed",Arial,sans-serif;font-weight:300;font-size:12.5px;color:#fff;margin-bottom:10px}
.fcol h4 b{font-weight:700}
.fcol ul{list-style:none}
.fcol li{font-size:8px;color:#dbe7f6;line-height:14.5px;display:flex;align-items:center;gap:5px}
.fcol li::before{content:"";width:2px;height:2px;background:#dbe7f6}
.social{display:flex;gap:5px;margin-top:9px}
.social span{width:18px;height:18px;border-radius:50%;background:rgba(255,255,255,.15)}
</style>
</head>
<body>
<div class="top-strip"></div>
<div class="sheet"></div>

<div class="abs banner-slot">Banner 970 x 200</div>

<div class="abs brand"><div class="brand-mark"></div><div class="brand-name">STARTFIRMO.eu</div></div>

<div class="abs contact">
  <div><svg viewBox="0 0 12 12"><circle cx="6" cy="6" r="5.5" fill="none" stroke="#b5bac0"/><path d="M4 3.5l1 1-.6.9c.4.8 1 1.4 1.8 1.8l.9-.6 1 1-.8.9C5.6 8.3 3.7 6.4 3.5 4.3z" fill="#9aa0a7"/></svg>224 - 555 - 018</div>
  <div><svg viewBox="0 0 12 12"><circle cx="6" cy="6" r="5.5" fill="none" stroke="#b5bac0"/><rect x="3.3" y="4" width="5.4" height="4" fill="none" stroke="#9aa0a7" stroke-width=".8"/><path d="M3.3 4l2.7 2 2.7-2" fill="none" stroke="#9aa0a7" stroke-width=".8"/></svg>info@startfirmo.eu</div>
</div>

<div class="abs btn btn-signin">Sign In</div>
<div class="abs btn btn-new">New User</div>

<nav class="abs mainnav">
  <a href="#">ZALOŽENÍ S.R.O.</a>
  <a href="#">ŽIVNOSTENSKÝ LIST</a>
  <a href="#">ZALOŽENÍ A.S.</a>
  <div class="nav-tools">
    <svg width="14" height="14" viewBox="0 0 14 14"><circle cx="7" cy="7" r="4.2" fill="none" stroke="#fff" stroke-width="2.6" stroke-dasharray="2 1.3"/><circle cx="7" cy="7" r="1.6" fill="#fff"/></svg>
    <svg width="14" height="14" viewBox="0 0 14 14"><circle cx="7" cy="7" r="6" fill="none" stroke="#fff" stroke-width="1.2"/><text x="7" y="10" font-size="8" fill="#fff" text-anchor="middle" font-family="Arial,sans-serif">?</text></svg>
    <div class="lang"><span style="width:11px;height:7px;background:#c8d4e6;display:block"></span><svg width="5" height="4" viewBox="0 0 5 4"><path d="M0 0h5L2.5 4z" fill="#fff"/></svg></div>
  </div>
</nav>

<section class="abs hero">
  <div class="hero-photo" role="img" aria-label="Soft background photo of young people working together at a laptop"></div>
  <h1 class="hero-title"><span>FREE</span> COMPANY IN FORMATIONS ONLINE</h1>
  <ul class="perks">
    <li><svg viewBox="0 0 12 10"><path d="M1 5l3.5 3.5L11 1.5" fill="none" stroke="var(--green-tick)" stroke-width="2"/></svg>Pay Statutory Registration Fees Only</li>
    <li><svg viewBox="0 0 12 10"><path d="M1 5l3.5 3.5L11 1.5" fill="none" stroke="var(--green-tick)" stroke-width="2"/></svg>Simply Without Attending State Authorities</li>
    <li><svg viewBox="0 0 12 10"><path d="M1 5l3.5 3.5L11 1.5" fill="none" stroke="var(--green-tick)" stroke-width="2"/></svg>Registered Capital From CZK 1</li>
    <li><svg viewBox="0 0 12 10"><path d="M1 5l3.5 3.5L11 1.5" fill="none" stroke="var(--green-tick)" stroke-width="2"/></svg>Company Formed in 3-5 Days</li>
  </ul>
  <div class="cta cta-try"><span>Try Unbinding Registration</span><i></i></div>
  <div class="cta cta-how"><span>How it Work</span><i></i></div>
  <div class="stats">
    <div class="lbl">Registered up to Date</div>
    <div class="num">4345 <span style="font-weight:300">fifms</span></div>
    <div class="testi">Testimonials</div>
  </div>
  <div class="seal" style="left:392px;top:118px;width:56px;height:56px;border:2px solid #c9d0da;background:#f1f3f6"></div>
  <div class="seal" style="left:478px;top:112px;width:62px;height:62px;border:2px solid #b9d3ec;background:#eef5fb"></div>
</section>

<aside class="abs sidenav">
  <ul>
    <li>How it Work</li>
    <li class="active">Before Beginning</li>
    <li>Form Company</li>
    <li>Check Registration</li>
    <li>FAQ</li>
    <li>Contacts</li>
  </ul>
  <div class="square-slot">Banner 200 x 200</div>
</aside>

<section class="abs why">
  <h2>Why StartFirmo.eu?</h2>
  <div class="why-item"><svg viewBox="0 0 9 7"><path d="M0 2h5V0l4 3.5L5 7V5H0z" fill="#8d939a"/></svg><p>The only system in the Czech Republic enabling the complex formation of new companies online through the Internet, without complicated administration, running around state authorities or visits of law firms.</p></div>
  <div class="why-item"><svg viewBox="0 0 9 7"><path d="M0 2h5V0l4 3.5L5 7V5H0z" fill="#8d939a"/></svg><p>Free of charge handling with the payment of statutory registration fees only. Save 60-80% of costs in comparison with the formation of companies through a law firm or the purchase of a ready-made company.</p></div>
  <div class="why-item"><svg viewBox="0 0 9 7"><path d="M0 2h5V0l4 3.5L5 7V5H0z" fill="#8d939a"/></svg><p>Short registration process, all documentation is generated automatically online and the registration is completed in short periods (usually 10-14 business days).</p></div>
  <div class="why-item"><svg viewBox="0 0 9 7"><path d="M0 2h5V0l4 3.5L5 7V5H0z" fill="#8d939a"/></svg><p>Formation of new company with no trading history or transferred from third parties. No risk of potential hidden liabilities or previous records in the Company Register as in case of ready-made (shelf) companies.</p></div>
  <div class="why-item"><svg viewBox="0 0 9 7"><path d="M0 2h5V0l4 3.5L5 7V5H0z" fill="#8d939a"/></svg><p>Simple and user-friendly online registration form enabling tailor-made company formation for each user.</p></div>
</section>

<div class="abs promo promo-statutory">
  <h3>STATUTORY</h3>
  <p class="sub">Costs Only, No Commitments</p>
  <div class="rows">
    <div class="row"><b>S.R.O</b>Formation From CZK 13,500</div>
    <div class="row"><b>ZL</b>Formation From CZK 1,000</div>
  </div>
</div>
<div class="abs promo promo-office">
  <h3>NEED ALSO</h3>
  <p class="sub">Registered Office?</p>
  <div class="rows">
    <div class="row"><b style="width:54px">Prague</b>From CZK 216/month</div>
    <div class="row"><b style="width:54px">Ostrava</b>From CZK 436/month</div>
  </div>
</div>

<div class="abs divider-shadow"></div>

<section class="abs news">
  <h2>Latest News</h2>
  <article class="news-item">
    <div class="news-date">30. 09. 2011</div>
    <div class="news-title">Applies to The Startups of the Year Awards</div>
    <p class="news-text">Startups of the Year 2011 is a new competition, designated for starting entrepreneurs where valuable prices and professional support may be found for the start of business. The competition was launched by TelNova and StartFirmo.eu is one.</p>
  </article>
  <article class="news-item">
    <div class="news-date">15. 08. 2011</div>
    <div class="news-title">The change of court fees for registrations in the Czech Company Register</div>
    <p class="news-text">As of 1.9.2011, the change to statutory court fees will become effective for the registration of new companies into the Czech Company Register . Instead of the current CZK 5,000 fee, the registration of joint stock companies will be subje.</p>
  </article>
</section>
<div class="abs btn btn-more">View more</div>

<footer class="abs footer">
  <div class="fcol" style="left:89px;width:124px"><h4>From <b>Company</b></h4><ul><li>S.R.O.</li><li>Trade License</li></ul></div>
  <div class="fcol" style="left:233px;width:134px;padding-left:11px"><h4>Client <b>Zone</b></h4><ul><li>My Registrations</li><li>Check Registration</li><li>My Profile</li></ul></div>
  <div class="fcol" style="left:383px;width:170px;padding-left:11px"><h4>Form <b>Company</b></h4><ul><li>How it Works</li><li>Before Beginning</li><li>Busines Conditions</li><li>Affiliate Program</li></ul></div>
  <div class="fcol" style="left:556px;width:100px;padding-left:11px"><h4>Support</h4><ul><li>Contact</li><li>FAQ</li></ul><div class="social"><span></span><span></span><span></span></div></div>
  <div class="footer-bottom">Copyright © 2013 NovaFirma.cz, all rights reserved</div>
</footer>
</body>
</html>
```